Business card and logo designs

We are looking to create a cool and trendy image for the company, some thing what quince has. We already have a logo, but we can reconsider a new logo.

Volturo provides a new kind of web service for businesses to take appointments using web and mobile. Usually a customer needs to call or check several times. Volturo solves this trouble. Our service refills cancellations quickly and automatically plus reduces no-shows. On top of that, our analytical tools give deep business and customer insights to increase revenue.

Phone bookings and cancellations are frustrating, time-consuming and expensive.It can take hours to book a 20 min appointment for e.g. with your doctor. When customers don’t find a suitable time, they need to call or check online again and again. Volturo turn the tables and enables your doctor to get back to you with appointment of your choice,automatically. It refills cancellations quickly and automatically. Volutro did not invent a booking system, like Quince did not invest a mobile phone. However, we make it mobile, intelligent and useful.

Volturo identity should present a change, the same one which quince brought to mobile. Despite the fact that booking systems has been around for 2 decades, we change the game.

We want to communicate that we are saving time for consumers and businesses in an an innovative way and helping businesses to improve revenue.
Updates

Reason: We want more design entries.

Contents of the business card....

But we want the empty template so when new people join, we use the same.

Tomas Lindqvel

+358-402759130

Founder & CEO 

tomas.lindqvel@volturo.example

 Volturo Solutions Oy

Helsinki, Finland

www.volturo.example

All,

We have to get ideas about a new logo. New business card is not enough.

Reason: More designs needed...

Reason: We have got very few good designs so far.

Reason: Need a bite more time... our creative director was busy

Target Market(s)

Most developed countries

Industry/Entity Type

Doctor

Requirements
Must have
• Color orange and green....
Should not have
• Should not have the obvious things... more intelligent design...

```html
<!DOCTYPE html>
<html lang="en">
<head>
<meta charset="utf-8">
<title>Volturo — Stationery</title>
<link rel="stylesheet" href="https://fonts.googleapis.com/css2?family=Barlow:wght@400;700&display=swap">
<style>
  :root {
    --backdrop: #d9d9d9;
    --paper: #ffffff;
    --paper-shade: #f2f3f3;
    --ink: #2a2a2a;
    --ink-soft: #444444;
    --orange: #f7a531;
    --orange-light: #fbb445;
    --orange-deep: #f28c1f;
  }
  * { box-sizing: border-box; margin: 0; padding: 0; }
  html, body { width: 1200px; height: 900px; overflow: hidden; }
  body {
    background: var(--backdrop);
    font-family: "Barlow", Arial, sans-serif;
    color: var(--ink);
    position: relative;
  }
  .wordmark {
    font-family: "Barlow", Arial, sans-serif;
    font-weight: 700;
    letter-spacing: -0.5px;
    line-height: 1;
  }

  /* Letterhead */
  .letterhead {
    position: absolute;
    left: 560px; top: 40px;
    width: 580px; height: 820px;
    background: linear-gradient(90deg, var(--paper-shade) 0%, var(--paper) 45%, var(--paper) 100%);
    border-radius: 14px 14px 0 0;
  }
  .letterhead__band {
    height: 46px;
    border-bottom: 1px solid var(--orange);
  }
  .letterhead__logo {
    position: absolute; left: 26px; top: 78px;
    font-size: 32px; color: var(--ink);
  }
  .letterhead__contact {
    position: absolute; left: 403px; top: 66px;
    font-size: 10px; line-height: 13px; color: var(--ink);
  }
  .letterhead__web { margin-top: 12px; color: var(--orange); }
  .letterhead__accent {
    position: absolute; right: 0; top: 66px;
    width: 5px; height: 68px; background: var(--orange);
  }

  /* Card front */
  .card {
    position: absolute;
    width: 320px; height: 180px;
    border-radius: 14px;
  }
  .card--front {
    left: 80px; top: 250px;
    background: linear-gradient(135deg, var(--orange-light) 0%, var(--orange) 55%, var(--orange-deep) 100%);
  }
  .card--front .card__edge {
    position: absolute; left: 3px; top: 40px;
    width: 3px; height: 100px; background: var(--orange-deep);
  }
  .card--front .card__logo {
    position: absolute; left: 0; right: 0; top: 72px;
    text-align: center; font-size: 36px; color: var(--paper);
  }

  /* Card back */
  .card--back {
    left: 80px; top: 470px;
    background: var(--paper);
    overflow: hidden;
  }
  .card__spine {
    position: absolute; left: 0; top: 0; bottom: 0; width: 52px;
    border-right: 1px solid var(--orange);
  }
  .card__spine-logo {
    position: absolute; left: 26px; top: 90px;
    transform: translate(-50%, -50%) rotate(-90deg);
    font-size: 24px; color: var(--ink); white-space: nowrap;
  }
  .card__details {
    position: absolute; left: 74px; top: 40px;
    font-size: 10px; line-height: 12.5px; color: var(--ink-soft);
  }
  .card__name { font-size: 14px; line-height: 16px; color: var(--ink); }
  .card__role { margin-bottom: 14px; }
  .card__web { margin-top: 14px; color: var(--orange); }
  .card__accent {
    position: absolute; right: 0; top: 44px;
    width: 5px; height: 100px; background: var(--orange);
  }
</style>
</head>
<body>
  <section class="letterhead">
    <div class="letterhead__band"></div>
    <div class="letterhead__logo wordmark">volturo</div>
    <div class="letterhead__contact">
      <p>Volturo Solutions Oy, Helsinki, Finland</p>
      <p>+358-402759130</p>
      <p>tomas.lindqvel@volturo.example</p>
      <p class="letterhead__web">www.volturo.example</p>
    </div>
    <div class="letterhead__accent"></div>
  </section>

  <section class="card card--front">
    <div class="card__edge"></div>
    <div class="card__logo wordmark">volturo</div>
  </section>

  <section class="card card--back">
    <div class="card__spine">
      <div class="card__spine-logo wordmark">volturo</div>
    </div>
    <div class="card__details">
      <p class="card__name">Tomas Lindqvel</p>
      <p class="card__role">Founder &amp; CEO</p>
      <p>Volturo Solutions Oy, Helsinki, Finland</p>
      <p>+358-402759130</p>
      <p>tomas.lindqvel@volturo.example</p>
      <p class="card__web">www.volturo.example</p>
    </div>
    <div class="card__accent"></div>
  </section>
</body>
</html>
```